Mindfulness School for Children -- Business Cards

We're looking for business cards for our school directors and owners. We're a mindfulness school for children called tumbling willows. Attached are our logos/icons.

```html
<!DOCTYPE html>
<html lang="en">
<head>
<meta charset="utf-8">
<title>tumbling willows — business cards</title>
<link rel="stylesheet" href="https://fonts.googleapis.com/css2?family=Lustria&family=Questrial&family=Lato:wght@400&display=swap">
<style>
  :root {
    --backdrop: #1c1c1c;
    --aqua-light: #93d6c9;
    --aqua-mid: #8ccfd6;
    --mint: #9dd8b4;
    --teal: #5aa494;
    --teal-deep: #4e9a8c;
    --sky: #63b9d0;
    --green-name: #8fcf9e;
    --blue-name: #5fb4d6;
    --ink: #3d3d3d;
    --white: #ffffff;
  }
  * { box-sizing: border-box; margin: 0; padding: 0; }
  html, body { width: 1200px; height: 1015px; overflow: hidden; }
  body {
    background: var(--backdrop);
    position: relative;
    font-family: "Lato", sans-serif;
  }
  .card {
    position: absolute;
    left: 240px;
    width: 720px;
    height: 412px;
    overflow: hidden;
    box-shadow: 0 10px 30px rgba(0,0,0,.5);
  }
  /* Front */
  .card--front {
    top: 60px;
    background:
      radial-gradient(circle at 70% 25%, var(--aqua-mid) 0%, transparent 45%),
      radial-gradient(circle at 85% 80%, var(--mint) 0%, transparent 50%),
      linear-gradient(135deg, var(--mint) 0%, var(--aqua-light) 55%, var(--aqua-mid) 100%);
  }
  .front-circle {
    position: absolute;
    left: 60px;
    top: 36px;
    width: 340px;
    height: 340px;
    border-radius: 50%;
    background: radial-gradient(circle at 40% 35%, #7fc3cd 0%, #6db5b3 55%, #64ab9f 100%);
  }
  .front-wordmark {
    position: absolute;
    right: 52px;
    bottom: 80px;
    font-family: "Lustria", serif;
    font-size: 44px;
    color: var(--white);
    letter-spacing: .5px;
  }
  /* Back */
  .card--back {
    top: 532px;
    background: var(--white);
  }
  .wave { position: absolute; inset: 0; }
  .back-wordmark {
    position: absolute;
    left: 58px;
    top: 118px;
    font-family: "Lustria", serif;
    font-size: 42px;
    line-height: 1.2;
    color: var(--teal);
  }
  .holder {
    position: absolute;
    right: 48px;
    top: 28px;
    text-align: right;
  }
  .holder__name {
    font-family: "Questrial", sans-serif;
    font-size: 32px;
    line-height: 1;
    color: var(--blue-name);
  }
  .holder__name .first { color: var(--green-name); }
  .holder__role {
    font-family: "Questrial", sans-serif;
    font-size: 15px;
    color: var(--ink);
    margin-top: 4px;
  }
  .contact {
    position: absolute;
    right: 40px;
    top: 192px;
    list-style: none;
    text-align: right;
    color: var(--white);
    font-size: 15px;
    line-height: 22px;
  }
  .contact li { display: flex; justify-content: flex-end; align-items: center; gap: 8px; }
  .contact .address { margin-top: 6px; }
  .contact .no-icon { padding-right: 22px; }
  .contact svg { width: 14px; height: 14px; flex: none; }
</style>
</head>
<body>

<section class="card card--front" aria-label="Card front">
  <div class="front-circle"></div>
  <p class="front-wordmark">tumbling willows</p>
</section>

<section class="card card--back" aria-label="Card back">
  <svg class="wave" viewBox="0 0 720 412" preserveAspectRatio="none" aria-hidden="true">
    <defs>
      <linearGradient id="wave-fill" x1="0" y1="0" x2="0" y2="1">
        <stop offset="0" stop-color="#95d3a6"/>
        <stop offset="1" stop-color="#4e9a8c"/>
      </linearGradient>
    </defs>
    <path d="M0,330 C200,350 300,320 370,230 C430,150 520,105 720,100"
          fill="none" stroke="#63b9d0" stroke-width="8"/>
    <path d="M0,344 C210,364 310,334 382,242 C442,164 530,118 720,112"
          fill="none" stroke="#5aa494" stroke-width="5"/>
    <path d="M0,358 C220,376 320,346 394,254 C454,176 540,130 720,124 L720,412 L0,412 Z"
          fill="url(#wave-fill)"/>
  </svg>

  <p class="back-wordmark">tumbling willows</p>

  <div class="holder">
    <p class="holder__name"><span class="first">Daniel</span> Brooks</p>
    <p class="holder__role">Managing Director</p>
  </div>

  <ul class="contact">
    <li>044-555 010 234
      <svg viewBox="0 0 16 16"><path d="M3 1.5l2.5 0 1 3.5-1.6 1.2a9 9 0 0 0 4.9 4.9L11 9.5l3.5 1v2.5a1.5 1.5 0 0 1-1.5 1.5A12 12 0 0 1 1.5 3 1.5 1.5 0 0 1 3 1.5z" fill="#fff"/></svg>
    </li>
    <li>hello@tumblingwillows.com
      <svg viewBox="0 0 16 16"><rect x="1" y="3" width="14" height="10" fill="#fff"/><path d="M1 3l7 6 7-6" fill="none" stroke="#7cc09b" stroke-width="1.2"/></svg>
    </li>
    <li>www.tumblingwillows.com
      <svg viewBox="0 0 16 16"><circle cx="8" cy="8" r="6.5" fill="none" stroke="#fff" stroke-width="1.4"/><ellipse cx="8" cy="8" rx="2.8" ry="6.5" fill="none" stroke="#fff" stroke-width="1.2"/><path d="M1.5 8h13M2.5 5h11M2.5 11h11" stroke="#fff" stroke-width="1.1"/></svg>
    </li>
    <li class="address">18, Meadow Lane
      <svg viewBox="0 0 16 16"><path d="M8 1a4.8 4.8 0 0 0-4.8 4.8C3.2 9.5 8 15 8 15s4.8-5.5 4.8-9.2A4.8 4.8 0 0 0 8 1z" fill="#fff"/><circle cx="8" cy="5.8" r="1.8" fill="#7cc09b"/></svg>
    </li>
    <li class="no-icon">Brookfield, 20417</li>
  </ul>
</section>

</body>
</html>
```